Mapping Bright Currents Through the Modern Seminar Room

This is for a book cover aimed at professors in higher education who want to infuse creative thinking into their classroom. It should have the title on the cover (see name of project). Our first idea is to have a stack of academic type books on a desk in black and white and then have a colorful rainbow light thread hitting the books. However, we are open to options! It has to be sophisticated, cool, and creative ;)

Target Market(s)

Higher Education Instructors

Industry/Entity Type

education

Font styles to use
Serif
Sans Serif

Requirements
Nice to have
• a creative feel of some sort
Should not have
• lightbulbs

```html
<!DOCTYPE html>
<html lang="en">
<head>
<meta charset="utf-8">
<title>Mapping Bright Currents Through the Modern Seminar Room — Cover</title>
<link rel="stylesheet" href="https://fonts.googleapis.com/css2?family=Montserrat:wght@300;500;700;800&family=Yellowtail&display=swap">
<style>
  :root {
    --backdrop: #808080;
    --cover-ink: #140f12;
    --glow-white: #ffffff;
    --glow-grey: #8a8a8a;
    --accent-orange: #f07a14;
    --title-white: #ffffff;
    --title-blue: #1769b5;
    --author-white: #f4f4f4;
  }
  * { box-sizing: border-box; margin: 0; padding: 0; }
  html, body {
    width: 1200px;
    height: 1200px;
    overflow: hidden;
    background: var(--backdrop);
  }
  .canvas {
    position: relative;
    width: 1200px;
    height: 1200px;
  }
  .cover {
    position: absolute;
    left: 250px;
    top: 75px;
    width: 700px;
    height: 1050px;
    background: var(--cover-ink);
    overflow: hidden;
  }
  .cover-art {
    position: absolute;
    left: 0;
    top: 225px;
    width: 700px;
    height: 735px;
    background:
      radial-gradient(ellipse 48% 55% at 50% 62%, var(--glow-white) 0%, #f2f2f2 30%, rgba(200,200,200,0.75) 55%, rgba(60,60,60,0) 85%),
      linear-gradient(180deg, #2a2a2a 0%, #4a4a4a 30%, #3a3a3a 70%, #2a1f18 100%);
    -webkit-mask-image: linear-gradient(180deg, transparent 0%, #000 12%, #000 90%, transparent 100%);
            mask-image: linear-gradient(180deg, transparent 0%, #000 12%, #000 90%, transparent 100%);
  }
  .title-line {
    position: absolute;
    left: 0;
    width: 100%;
    text-align: center;
    line-height: 1;
    white-space: nowrap;
  }
  .title-lead {
    top: 138px;
    font-family: "Montserrat", sans-serif;
    font-weight: 300;
    font-size: 52px;
    letter-spacing: 0.02em;
    color: var(--accent-orange);
  }
  .title-light {
    top: 200px;
    font-family: "Montserrat", sans-serif;
    font-weight: 300;
    font-size: 100px;
    color: var(--title-white);
  }
  .title-bold {
    top: 306px;
    font-family: "Montserrat", sans-serif;
    font-weight: 800;
    font-size: 88px;
    letter-spacing: -0.01em;
    color: var(--title-white);
    text-shadow: 0 0 12px rgba(0,0,0,0.35);
  }
  .title-link {
    top: 410px;
    font-family: "Yellowtail", cursive;
    font-size: 50px;
    color: var(--title-white);
  }
  .title-blue {
    font-family: "Montserrat", sans-serif;
    font-weight: 700;
    font-size: 66px;
    letter-spacing: -0.01em;
    color: var(--title-blue);
  }
  .title-blue.line-1 { top: 472px; }
  .title-blue.line-2 { top: 542px; }
  .title-blue.line-3 { top: 615px; }
  .author-name {
    top: 970px;
    font-family: "Montserrat", sans-serif;
    font-weight: 500;
    font-size: 32px;
    letter-spacing: 0.14em;
    color: var(--author-white);
  }
</style>
</head>
<body>
  <main class="canvas">
    <article class="cover">
      <div class="cover-art" role="img" aria-label="Open book glowing with white light and sparkling stars on a dark wooden table against a textured dark wall"></div>
      <h1 class="cover-title">
        <span class="title-line title-lead">MAPPING</span>
        <span class="title-line title-light">BRIGHT</span>
        <span class="title-line title-bold">CURRENTS</span>
        <span class="title-line title-link">through</span>
        <span class="title-line title-blue line-1">THE MODERN</span>
        <span class="title-line title-blue line-2">SEMINAR</span>
        <span class="title-line title-blue line-3">ROOM</span>
      </h1>
      <p class="title-line author-name">AUTHOR NAME</p>
    </article>
  </main>
</body>
</html>
```